Meridel Haulage - Website

A clean, not cluttered informative website for our business. We specialize in the transportation of radioactive materials across North America. The site is mostly for information about our company and will not be used to attract business but will be used to attract employee's mainly drivers. Driver's are very hard to find in our area. One of the pages needs to be a job's posting page with an apply now button. Either an application can be filled out there or a resume can be uploaded which ever functionality works better. I would like a website that I can easily edit, ability to change text and photos.

Number of Pages Required

5+ page

Colors

Designer to choose colors to be used in the design.

Requirements
Must have
• Home - About - Services - Jobs - Contact pages
• A way prospective employee's can apply or upload their resume to be emailed to me
• Very clean apperance
Should not have
• I don't want it to be busy

```html
<!DOCTYPE html>
<html lang="en">
<head>
<meta charset="utf-8">
<title>Meridel Haulage</title>
<link href="https://fonts.googleapis.com/css2?family=Poppins:wght@400;500;600&family=Exo+2:wght@500;600;700&display=swap" rel="stylesheet">
<style>
:root{
  --blue:#1a6fb8;
  --blue-dark:#135a98;
  --gray:#777b80;
  --text:#333;
  --line:#e6e6e6;
  --footer:#1c70b9;
  --bar:#75777a;
  --white:#fff;
}
*{margin:0;padding:0;box-sizing:border-box}
html,body{width:1200px;height:2639px;overflow:hidden;background:#fff}
body{position:relative;font-family:"Poppins",sans-serif;color:var(--text)}
.abs{position:absolute}
.heading{font-family:"Exo 2",sans-serif}

/* header */
.site-header{left:0;top:0;width:1200px;height:128px;background:#fff}
.brand{left:80px;top:40px;display:flex;align-items:center;gap:10px;font-family:"Poppins",sans-serif;font-weight:600;font-size:30px;color:var(--blue)}
.brand-dot{width:16px;height:16px;border-radius:50%;background:var(--blue)}
.contact-top{top:20px;font-size:16px;color:#444;display:flex;align-items:center;gap:8px}
.nav{top:76px;left:588px;display:flex;gap:0;font-size:17px}
.nav a{color:#333;text-decoration:none;position:absolute;white-space:nowrap}
.nav a.active{color:var(--blue)}

/* hero */
.hero{left:0;top:128px;width:1200px;height:492px;background:linear-gradient(160deg,#9aa0a6 0%,#6f737a 35%,#4b5058 60%,#2f3f66 80%,#4a4d52 100%)}
.hero-arrow{top:340px;width:36px;height:34px;background:rgba(0,0,0,.55);display:flex;align-items:center;justify-content:center}
.hero-title{left:0;top:455px;width:1200px;text-align:center;color:#fff;font-size:42px;line-height:51px;font-weight:500;text-shadow:0 2px 6px rgba(0,0,0,.7)}

/* section titles */
.section-title{left:0;width:1200px;text-align:center;font-size:38px;font-weight:600}
.section-title .accent{color:var(--blue)}
.section-title .muted{color:var(--gray)}
.title-rule{height:2px;background:#9a9a9a;left:50%}

.about-sub{left:0;top:755px;width:1200px;text-align:center;color:var(--blue);font-size:20px}
.about-text{left:100px;top:788px;width:1000px;text-align:center;font-size:15.5px;line-height:29px;color:#333}
.btn{display:flex;align-items:center;justify-content:center;background:var(--blue);color:#fff;font-size:19px;box-shadow:3px 4px 6px rgba(0,0,0,.3);text-decoration:none}

.divider{left:100px;top:1043px;width:1000px;height:1px;background:var(--line)}

/* services */
.service-img{width:237px;height:198px;border-left:2px solid var(--blue);border-bottom:2px solid var(--blue)}
.service-name{width:265px;text-align:center;font-size:19px;font-weight:600;color:#222}
.service-text{width:265px;text-align:center;font-size:14.5px;line-height:26px;color:#333}

/* opportunities */
.opp-img{left:75px;top:1790px;width:545px;height:403px;border-left:2px solid var(--blue);border-bottom:2px solid var(--blue);background:linear-gradient(120deg,#2e3a4a 0%,#6e7a88 40%,#cfd4d8 70%,#a9b0b6 100%)}
.opp-card{left:580px;top:1833px;width:540px;height:317px;background:#fff;box-shadow:0 0 10px rgba(0,0,0,.12);padding:62px 24px 0 24px}
.opp-card h3{font-size:21px;font-weight:600;color:#222;margin-bottom:12px}
.opp-card p{font-size:13.5px;line-height:27px;color:#333}
.opp-card p b{font-size:17px;font-weight:600;color:#111}

/* footer */
.site-footer{left:0;top:2277px;width:1200px;height:313px;background:var(--footer);color:#fff}
.f-head{top:2312px;font-size:17px;font-weight:600}
.f-rule{top:2350px;width:48px;height:2px;background:#fff}
.f-links{left:82px;top:2375px;font-size:15px;line-height:36px}
.f-item{font-size:15px;line-height:25px;display:flex;gap:14px;align-items:flex-start}
.map{left:572px;top:2376px;width:285px;height:167px;background:linear-gradient(135deg,#e8ece6,#d6dce0);border-bottom:22px solid #000}
.social{top:2380px;width:30px;height:30px;border-radius:50%;background:#8a8d91}
.apply-box{left:918px;top:2420px;width:202px;height:77px;background:#8f9195;border:2px solid #bfc1c3;color:#fff;text-align:center;font-weight:600;font-size:15px;line-height:22px;padding-top:14px}
.copy-bar{left:0;top:2590px;width:1200px;height:49px;background:var(--bar);color:#fff;font-size:14px}
.sq{top:2600px;width:30px;height:30px}
</style>
</head>
<body>

<header class="site-header abs">
  <div class="brand abs"><span class="brand-dot"></span>Meridel Haulage</div>
  <div class="contact-top abs" style="left:680px">
    <svg width="30" height="22" viewBox="0 0 30 22"><rect x="1" y="1" width="28" height="20" fill="none" stroke="#1a6fb8" stroke-width="2"/><path d="M1 1l14 11L29 1M1 21l10-9M29 21l-10-9" fill="none" stroke="#1a6fb8" stroke-width="2"/></svg>
    inquiry@meridelhaulage.com
  </div>
  <div class="contact-top abs" style="left:962px;font-size:18px">
    <svg width="28" height="28" viewBox="0 0 28 28"><circle cx="14" cy="14" r="12.5" fill="none" stroke="#1a6fb8" stroke-width="2"/><path d="M9 7c-2 2 0 7 4 11s8 5 9 3l-3-3-2 2c-2-1-4-3-5-5l2-2z" fill="#1a6fb8"/></svg>
    123.456.7890
  </div>
  <nav class="nav abs">
    <a class="active" style="left:0">Home</a>
    <a style="left:99px">About Us</a>
    <a style="left:224px">Services</a>
    <a style="left:344px">Jobs</a>
    <a style="left:432px">Contact Us</a>
  </nav>
</header>

<section class="hero abs" role="img" aria-label="Semi truck hauling radioactive material containers on a flatbed trailer"></section>
<div class="hero-arrow abs" style="left:6px"><svg width="10" height="14"><path d="M8 1L2 7l6 6" fill="none" stroke="#fff" stroke-width="2.5"/></svg></div>
<div class="hero-arrow abs" style="left:1158px"><svg width="10" height="14"><path d="M2 1l6 6-6 6" fill="none" stroke="#fff" stroke-width="2.5"/></svg></div>
<h1 class="hero-title abs">We Specialize In The<br>Transportation of Radioactive<br>Materials Across North America</h1>

<section class="about">
  <h2 class="section-title heading abs" style="top:676px"><span class="accent">About Meridel</span> <span class="muted">Haulage</span></h2>
  <div class="title-rule abs" style="top:732px;width:180px;margin-left:-90px"></div>
  <p class="about-sub abs">We Serve Accross Whole North America</p>
  <p class="about-text abs">Lorem ipsum dolor sit amet, consectetuer adipiscing elit, sed diam nonummy nibh euismod tincidunt ut laoreet dolore magna aliquam erat volutpat. Ut wisi enim ad minim veniam, quis nostrud exerci tation ullamcorper suscipit lobortis nisl aliquip ex ea commodo consequat. Duis autem vel eum iriure dolor in hendrerit ivulputate velit esse molestie consequat, vel illum dolore eu feugiat nulla facilisis</p>
  <a class="btn abs" style="left:531px;top:920px;width:136px;height:47px">Read More</a>
</section>

<div class="divider abs"></div>

<section class="services">
  <h2 class="section-title heading abs" style="top:1118px"><span class="accent">OUR</span> <span class="muted">SERVICES FOR</span></h2>
  <div class="title-rule abs" style="top:1172px;width:84px;margin-left:-42px"></div>

  <div class="service-img abs" role="img" aria-label="Experienced driver behind the wheel of a truck" style="left:81px;top:1225px;background:linear-gradient(135deg,#3a4048,#7d8a94 50%,#b7c7c0)"></div>
  <div class="service-img abs" role="img" aria-label="New drivers training on a driving simulator" style="left:347px;top:1225px;background:linear-gradient(135deg,#5b6470,#a9b3bc 50%,#3e4c62)"></div>
  <div class="service-img abs" role="img" aria-label="Driver giving a thumbs up beside a truck" style="left:613px;top:1225px;background:linear-gradient(135deg,#5a86c4,#8fb0d8 50%,#3c5b8e)"></div>
  <div class="service-img abs" role="img" aria-label="Military veteran standing with arms crossed" style="left:877px;top:1225px;background:linear-gradient(135deg,#e4e6ea,#b9c0c8 50%,#27406a)"></div>

  <h3 class="service-name heading abs" style="left:70px;top:1440px">Experienced Drivers</h3>
  <h3 class="service-name heading abs" style="left:334px;top:1440px">Inexperienced Drivers</h3>
  <h3 class="service-name heading abs" style="left:600px;top:1440px">CDL Training</h3>
  <h3 class="service-name heading abs" style="left:864px;top:1440px">Military Veterans</h3>

  <p class="service-text abs" style="left:70px;top:1478px">Lorem ipsum dolor sit amet, consectetuer adipiscing elit, sed diam nonummy nibh euismod tincidunt ut laoreet dolore magna aliquam erat volutpat.</p>
  <p class="service-text abs" style="left:334px;top:1478px">Lorem ipsum dolor sit amet, consectetuer adipiscing elit, sed diam nonummy nibh euismod tincidunt ut laoreet dolore magna aliquam erat volutpat.</p>
  <p class="service-text abs" style="left:600px;top:1478px">Lorem ipsum dolor sit amet, consectetuer adipiscing elit, sed diam nonummy nibh euismod tincidunt ut laoreet dolore magna aliquam erat volutpat.</p>
  <p class="service-text abs" style="left:864px;top:1478px">Lorem ipsum dolor sit amet, consectetuer adipiscing elit, sed diam nonummy nibh euismod tincidunt ut laoreet dolore magna aliquam erat volutpat.</p>

  <a class="btn abs" style="left:131px;top:1625px;width:135px;height:48px">Read More</a>
  <a class="btn abs" style="left:396px;top:1625px;width:135px;height:48px">Read More</a>
  <a class="btn abs" style="left:661px;top:1625px;width:135px;height:48px">Read More</a>
  <a class="btn abs" style="left:926px;top:1626px;width:135px;height:48px">Read More</a>
</section>

<section class="opportunities">
  <div class="opp-img abs" role="img" aria-label="Smiling driver standing next to a white truck cab"></div>
  <div class="opp-card abs">
    <h3 class="heading">Driving Opportunities</h3>
    <p>Lorem ipsum dolor sit amet, consectetuer adipiscing elit,m dolor sit amet, consectetuer adipiscing elit se diamnomy To speak with the Driver Recruiting Department, <b>Call 123.456.7890</b></p>
    <a class="btn" style="width:136px;height:48px;margin-top:16px;font-size:19px">APPLY NOW</a>
  </div>
</section>

<footer class="site-footer abs"></footer>
<div class="f-head heading abs" style="left:84px;color:#fff">Quick Links</div>
<div class="f-rule abs" style="left:84px"></div>
<div class="f-links abs" style="color:#fff">Home<br>About Us<br>Services<br>Jobs<br>Contact Us</div>

<div class="f-head heading abs" style="left:242px;color:#fff">Contact Details</div>
<div class="f-rule abs" style="left:242px"></div>
<div class="f-item abs" style="left:242px;top:2372px;color:#fff">
  <svg width="20" height="26" viewBox="0 0 20 26"><path d="M10 1a8 8 0 0 0-8 8c0 6 8 16 8 16s8-10 8-16a8 8 0 0 0-8-8z" fill="#fff"/><circle cx="10" cy="9" r="3" fill="#1c70b9"/></svg>
  <span>Street Name, City Name<br>State Zipcode</span>
</div>
<div class="f-item abs" style="left:242px;top:2455px;color:#fff">
  <svg width="22" height="22" viewBox="0 0 28 28"><circle cx="14" cy="14" r="12.5" fill="none" stroke="#fff" stroke-width="2"/><path d="M9 7c-2 2 0 7 4 11s8 5 9 3l-3-3-2 2c-2-1-4-3-5-5l2-2z" fill="#fff"/></svg>
  <span>123.456.7890</span>
</div>
<div class="f-item abs" style="left:242px;top:2516px;color:#fff">
  <svg width="24" height="18" viewBox="0 0 30 22"><rect x="1" y="1" width="28" height="20" fill="none" stroke="#fff" stroke-width="2"/><path d="M1 1l14 11L29 1" fill="none" stroke="#fff" stroke-width="2"/></svg>
  <span>inquiry@meridelhaulage.com</span>
</div>

<div class="f-head heading abs" style="left:572px;color:#fff">Location Map</div>
<div class="f-rule abs" style="left:572px"></div>
<div class="map abs" role="img" aria-label="Street map showing the company location"></div>

<div class="f-head heading abs" style="left:916px;color:#fff">Follow Us On</div>
<div class="f-rule abs" style="left:916px"></div>
<div class="social abs" style="left:918px"></div>
<div class="social abs" style="left:960px"></div>
<div class="social abs" style="left:1004px"></div>
<div class="apply-box abs">APPLY NOW<br>MH Driver Application</div>

<div class="copy-bar abs"><span class="abs" style="left:82px;top:15px">Copyright © 2019 Meridel Haulage. All Rights Reserved.</span></div>
<div class="sq abs" style="left:958px;background:#3b5a98"></div>
<div class="sq abs" style="left:1000px;background:#2aa3e0"></div>
<div class="sq abs" style="left:1042px;background:#0c6ea8"></div>
<div class="sq abs" style="left:1085px;background:#cc2a20"></div>

</body>
</html>
```